Brisa Vale residential and commercial cleaning

We need a Business card design for a new residential and commercial cleaning company based in UAE- Abu Dhabi named (BRISA VALE)
we provide a residential cleaning service based in hourly rate (Maid Rent - Baby Setting), Also a commercial and offices cleaning.
Our logo is attached for your reference

Target Market(s)

Women who are 22 to 60 years old.

Industry/Entity Type

Residential

Requirements
Should not have
• it should not have an old-style fonts

```html
<!DOCTYPE html>
<html lang="en">
<head>
<meta charset="utf-8">
<title>Brisa Vale Business Card</title>
<link rel="stylesheet" href="https://fonts.googleapis.com/css2?family=Montserrat:wght@400;600;700&display=swap">
<style>
  :root {
    --brand-blue: #1565b0;
    --brand-green: #7dc242;
    --card-white: #ffffff;
    --stage: #e7e9ec;
    --text-light: #ffffff;
    --text-soft: #dbe8f5;
  }
  * { box-sizing: border-box; margin: 0; padding: 0; }
  html, body {
    width: 1200px; height: 599px; overflow: hidden;
    background: var(--stage);
    font-family: "Montserrat", sans-serif;
  }
  .stage {
    position: relative; width: 1200px; height: 599px;
    display: flex; align-items: center; justify-content: center; gap: 60px;
  }
  .card {
    position: relative; width: 520px; height: 300px;
    border-radius: 18px; overflow: hidden;
    background: var(--card-white);
    box-shadow: 0 10px 24px rgba(0,0,0,.18);
  }

  /* Front card */
  .front-brand {
    position: absolute; left: 0; top: 0; width: 245px; height: 100%;
    display: flex; align-items: center; justify-content: center; gap: 10px;
  }
  .brand-name {
    font-weight: 700; font-size: 30px; line-height: 1.05;
    color: var(--brand-blue); letter-spacing: -0.5px;
  }
  .brand-dot {
    width: 26px; height: 26px; border-radius: 50%;
    background: var(--brand-green); flex: none;
  }
  .front-panel {
    position: absolute; left: 245px; top: 0; right: 0; height: 100%;
    background: var(--brand-blue);
  }
  .panel-stripe {
    position: absolute; top: 0; width: 6px; height: 100%;
    background: var(--card-white);
  }
  .panel-stripe.first { left: 12px; }
  .panel-stripe.second { left: 26px; }
  .person {
    position: absolute; left: 48px; top: 30px; color: var(--text-light);
  }
  .person-name {
    position: relative; font-weight: 700; font-size: 17px; letter-spacing: 1px;
    padding-left: 18px;
  }
  .person-name::before {
    content: ""; position: absolute; left: 0; top: 3px;
    border-left: 12px solid var(--brand-green);
    border-top: 7px solid transparent; border-bottom: 7px solid transparent;
  }
  .person-role {
    font-size: 13px; color: var(--text-soft); margin-top: 2px; padding-left: 84px;
  }
  .contacts {
    position: absolute; left: 56px; top: 145px; list-style: none;
    color: var(--text-light); font-size: 13px; letter-spacing: .5px;
  }
  .contacts li { display: flex; align-items: center; gap: 14px; height: 30px; }
  .contact-icon {
    width: 18px; height: 18px; border-radius: 3px; background: var(--card-white);
    display: flex; align-items: center; justify-content: center; flex: none;
  }

  /* Back card */
  .back-brand {
    position: absolute; left: 0; top: 0; width: 100%; height: 160px;
    display: flex; align-items: center; justify-content: center; gap: 12px;
  }
  .back-brand .brand-name { font-size: 38px; }
  .back-brand .brand-dot { width: 32px; height: 32px; }
  .back-band {
    position: absolute; left: 0; bottom: 0; width: 100%; height: 140px;
    background: var(--brand-blue);
  }
  .band-line {
    position: absolute; left: 0; top: 12px; width: 100%; height: 5px;
    background: var(--card-white);
  }
  .band-pointer {
    position: absolute; left: 50%; top: 17px; transform: translateX(-50%);
    border-top: 12px solid var(--brand-green);
    border-left: 10px solid transparent; border-right: 10px solid transparent;
  }
  .slogan {
    position: absolute; left: 0; top: 52px; width: 100%; text-align: center;
    color: var(--text-light); font-weight: 600; font-size: 14px; letter-spacing: 1.5px;
  }
</style>
</head>
<body>
<main class="stage">
  <section class="card card-front" aria-label="Business card front">
    <div class="front-brand">
      <span class="brand-name">Brisa<br>Vale</span>
      <span class="brand-dot"></span>
    </div>
    <div class="front-panel">
      <span class="panel-stripe first"></span>
      <span class="panel-stripe second"></span>
      <div class="person">
        <p class="person-name">AMIR HADDAD</p>
        <p class="person-role">Owner</p>
      </div>
      <ul class="contacts">
        <li>
          <span class="contact-icon">
            <svg width="12" height="12" viewBox="0 0 12 12" aria-hidden="true">
              <rect x="3" y="1" width="6" height="3" fill="#1565b0"/>
              <rect x="1" y="4" width="10" height="5" rx="1" fill="#1565b0"/>
              <rect x="3" y="7" width="6" height="4" fill="#fff" stroke="#1565b0"/>
            </svg>
          </span>
          <span>555-310-2847</span>
        </li>
        <li>
          <span class="contact-icon">
            <svg width="12" height="12" viewBox="0 0 12 12" aria-hidden="true">
              <path d="M2 4 Q6 1 10 4 L9 5.5 L7.5 4.5 L4.5 4.5 L3 5.5 Z" fill="#1565b0"/>
              <rect x="2.5" y="6" width="7" height="5" rx="1" fill="#1565b0"/>
            </svg>
          </span>
          <span>555-310-6192</span>
        </li>
        <li>
          <span class="contact-icon">
            <svg width="12" height="12" viewBox="0 0 12 12" aria-hidden="true">
              <rect x="1" y="3" width="10" height="7" fill="none" stroke="#1565b0" stroke-width="1.3"/>
              <path d="M1 3 L6 7 L11 3" fill="none" stroke="#1565b0" stroke-width="1.3"/>
            </svg>
          </span>
          <span>amir@brisavale.com</span>
        </li>
      </ul>
    </div>
  </section>

  <section class="card card-back" aria-label="Business card back">
    <div class="back-brand">
      <span class="brand-name">Brisa Vale</span>
      <span class="brand-dot"></span>
    </div>
    <div class="back-band">
      <span class="band-line"></span>
      <span class="band-pointer"></span>
      <p class="slogan">Your Website/Slogan here</p>
    </div>
  </section>
</main>
</body>
</html>
```